Powerpoint Presentation Template

Kindly design a business class Powepoint Presentation template for our business use. Please stick to our company colours or even pictures as shown on our website and Logo

```html
<!DOCTYPE html>
<html lang="en">
<head>
<meta charset="utf-8">
<title>Veldmark Properties – Presentation Template</title>
<link rel="stylesheet" href="https://fonts.googleapis.com/css2?family=Open+Sans:wght@300;400;600;700&display=swap">
<style>
:root{
  --maroon:#8b2a1e;
  --maroon-dark:#7a2418;
  --page:#c8c8c8;
  --slide:#ffffff;
  --band:#c4c4c4;
  --ink:#222222;
  --muted:#6b6b6b;
  --icon:#6d6e71;
  --box:#d6d6d6;
  --link:#1f57a8;
  --blue:#4a90d9;
  --orange:#ee7d31;
  --grey:#a5a5a5;
  --gold:#f5b921;
}
*{box-sizing:border-box;margin:0;padding:0}
html,body{width:1200px;height:1200px;overflow:hidden}
body{background:var(--page);font-family:"Open Sans",Arial,sans-serif;color:var(--ink);position:relative}
.slide{position:absolute;width:356px;height:266px;background:var(--slide);overflow:hidden;box-shadow:1px 2px 4px rgba(0,0,0,.25)}
.c1{left:38px}.c2{left:422px}.c3{left:806px}
.r1{top:107px}.r2{top:402px}.r3{top:698px}
.abs{position:absolute}
.title{position:absolute;left:0;right:0;top:18px;text-align:center;font-weight:700;font-size:13.5px;letter-spacing:.1px}
.rule{position:absolute;left:18px;right:18px;top:34px;height:1px;background:var(--maroon)}
.subtitle{position:absolute;left:0;right:0;text-align:center;color:var(--maroon);font-size:9.5px}
.footer{position:absolute;left:0;bottom:0;width:180px;height:15px}
.footer svg{position:absolute;left:0;top:0}
.footer span{position:absolute;left:18px;top:3px;color:#fff;font-size:6px;font-weight:600}
.pageno{position:absolute;right:16px;bottom:4px;font-size:5px;color:var(--link);font-weight:700}
.photo{position:absolute}
.brand{position:absolute;color:var(--maroon);font-weight:600;text-align:center;line-height:1}
.brand b{display:block;font-weight:600;font-size:17px;letter-spacing:-.5px}
.brand i{display:block;font-style:normal;font-size:11px;margin-top:1px}
.gband{position:absolute;left:0;right:0;background:var(--band)}
/* table of contents */
.toc-item{position:absolute;width:86px;height:20px}
.toc-num{position:absolute;left:0;top:2px;width:14px;height:14px;border-radius:50%;background:var(--maroon);border:1.5px solid #d9b3ad;color:#fff;font-size:5px;text-align:center;line-height:11px;font-weight:600}
.toc-bar{position:absolute;left:18px;top:1px;width:1px;height:17px;background:var(--maroon)}
.toc-head{position:absolute;left:22px;top:0;font-size:7.5px;color:var(--maroon);line-height:9px;white-space:nowrap}
.toc-text{position:absolute;left:22px;top:9px;font-size:3.6px;line-height:5px;color:#777;width:62px}
/* services */
.svc-icon{position:absolute;width:46px;height:46px;border-radius:50%;border:2px solid var(--maroon);padding:2px}
.svc-icon div{width:100%;height:100%;border-radius:50%;background:var(--icon);display:flex;align-items:center;justify-content:center}
.svc-text{position:absolute;width:74px;text-align:center;font-size:4.8px;line-height:7.9px;color:#666}
/* what we do */
.wwd-photo{position:absolute;width:60px;height:60px;border-radius:50%;border:1.5px solid #5d8a4a}
.wwd-box{position:absolute;top:114px;height:126px;background:var(--box);padding:3px 7px}
.wwd-box h4{color:var(--maroon);font-size:5.6px;line-height:7px;font-weight:400;border-bottom:.5px solid #999;padding-bottom:2px;margin-bottom:3px}
.wwd-box p{font-size:4.6px;line-height:7.9px;color:#222}
/* picture slide */
.ps-icon{position:absolute;width:14px;height:14px;border-radius:50%;border:1.2px solid var(--icon);display:flex;align-items:center;justify-content:center}
.ps-icon span{width:9px;height:9px;border-radius:50%;background:var(--icon)}
.ps-head{position:absolute;color:var(--maroon);font-size:6.6px;font-weight:700}
.ps-body{position:absolute;font-size:4.6px;line-height:7.9px;color:#222;width:116px}
/* bullets */
.bullet{position:absolute;left:230px;width:112px;font-size:3.8px;line-height:5.6px;color:#444;padding-left:7px}
.bullet:before{content:"";position:absolute;left:0;top:1px;width:3.5px;height:3.5px;border:.6px solid var(--link)}
/* chart slide */
.chart-title{position:absolute;left:32px;width:160px;text-align:center;font-size:8px;line-height:9px}
.legend{position:absolute;left:62px;top:102px;font-size:4px;display:flex;gap:4px}
.legend span:before{content:"";display:inline-block;width:3px;height:3px;margin-right:1px}
.lg-m:before{background:var(--blue)}.lg-s:before{background:var(--orange)}.lg-r:before{background:var(--grey)}.lg-l:before{background:var(--gold)}
.body-just{position:absolute;left:194px;width:146px;font-size:5.3px;line-height:7.9px;text-align:justify;color:#222}
/* closing */
.contact{position:absolute;font-size:6px;line-height:12px;color:#333}
.vline{position:absolute;width:1px;background:#999}
</style>
</head>
<body>

<!-- Cover -->
<section class="slide c1 r1">
  <div class="brand" style="left:128px;top:22px;width:100px"><b>VELDMARK</b><i>Properties</i></div>
  <div class="gband" style="top:63px;height:5px"></div>
  <div class="photo" role="img" aria-label="Dirt road under construction with barriers" style="left:0;top:72px;width:127px;height:50px;background:linear-gradient(#6f9fd4 0 35%,#c87a3e 35%,#a55a2a)"></div>
  <div class="photo" role="img" aria-label="Curving paved road through green bush" style="left:129px;top:72px;width:81px;height:50px;background:linear-gradient(160deg,#5f7a44,#8e9a86 60%,#6d6f6b)"></div>
  <div class="photo" role="img" aria-label="Modern residential houses" style="left:212px;top:72px;width:61px;height:50px;background:linear-gradient(#a9c1de,#b7b7b2 55%,#6e6f69)"></div>
  <div class="photo" role="img" aria-label="Brick apartment block" style="left:275px;top:72px;width:81px;height:50px;background:linear-gradient(#8fb4e0,#7a4a32 50%,#3a2b24)"></div>
  <div class="photo" role="img" aria-label="Modern office building under construction" style="left:0;top:125px;width:223px;height:90px;background:linear-gradient(#7eaee8,#b9c6d3 45%,#8a8a86 65%,#a07850)"></div>
  <div class="photo" role="img" aria-label="Company signboard at a housing estate" style="left:226px;top:125px;width:130px;height:90px;background:linear-gradient(#b7c9d6,#9aa48c 45%,#c2a58e 75%,#6c7a4a)"></div>
  <div class="gband" style="top:215px;height:5px"></div>
  <div class="abs" style="left:0;right:0;top:226px;text-align:center;color:var(--maroon);font-weight:300;font-size:18px;letter-spacing:-.3px">YOUR HEADLINE TEXT</div>
</section>

<!-- Table of content -->
<section class="slide c2 r1">
  <div class="title">TABLE OF CONTENT</div>
  <div class="rule"></div>
  <div class="toc-item" style="left:19px;top:57px"><div class="toc-num">1</div><div class="toc-bar"></div><div class="toc-head">About Us</div><div class="toc-text">Lorem ipsum is simply dummy text of the printing and typeset-</div></div>
  <div class="toc-item" style="left:139px;top:57px"><div class="toc-num">2</div><div class="toc-bar"></div><div class="toc-head">Who We Are</div><div class="toc-text">Lorem ipsum is simply dummy text of the printing and typeset-</div></div>
  <div class="toc-item" style="left:252px;top:57px"><div class="toc-num">3</div><div class="toc-bar"></div><div class="toc-head">What We Do</div><div class="toc-text">Lorem ipsum is simply dummy text of the printing and typeset-</div></div>
  <div class="toc-item" style="left:19px;top:102px"><div class="toc-num">4</div><div class="toc-bar"></div><div class="toc-head">About Us</div><div class="toc-text">Lorem ipsum is simply dummy text of the printing and typeset-</div></div>
  <div class="toc-item" style="left:139px;top:102px"><div class="toc-num">5</div><div class="toc-bar"></div><div class="toc-head">About Us</div><div class="toc-text">Lorem ipsum is simply dummy text of the printing and typeset-</div></div>
  <div class="toc-item" style="left:252px;top:102px"><div class="toc-num">6</div><div class="toc-bar"></div><div class="toc-head">About Us</div><div class="toc-text">Lorem ipsum is simply dummy text of the printing and typeset-</div></div>
  <div class="toc-item" style="left:19px;top:147px"><div class="toc-num">7</div><div class="toc-bar"></div><div class="toc-head">About Us</div><div class="toc-text">Lorem ipsum is simply dummy text of the printing and typeset-</div></div>
  <div class="toc-item" style="left:139px;top:147px"><div class="toc-num">8</div><div class="toc-bar"></div><div class="toc-head">About Us</div><div class="toc-text">Lorem ipsum is simply dummy text of the printing and typeset-</div></div>
  <div class="toc-item" style="left:252px;top:147px"><div class="toc-num">9</div><div class="toc-bar"></div><div class="toc-head">About Us</div><div class="toc-text">Lorem ipsum is simply dummy text of the printing and typeset-</div></div>
  <div class="toc-item" style="left:19px;top:192px"><div class="toc-num">7</div><div class="toc-bar"></div><div class="toc-head">About Us</div><div class="toc-text">Lorem ipsum is simply dummy text of the printing and typeset-</div></div>
  <div class="toc-item" style="left:139px;top:192px"><div class="toc-num">8</div><div class="toc-bar"></div><div class="toc-head">About Us</div><div class="toc-text">Lorem ipsum is simply dummy text of the printing and typeset-</div></div>
  <div class="toc-item" style="left:252px;top:192px"><div class="toc-num">9</div><div class="toc-bar"></div><div class="toc-head">About Us</div><div class="toc-text">Lorem ipsum is simply dummy text of the printing and typeset-</div></div>
  <div class="footer"><svg width="180" height="15"><polygon points="0,0 140,0 155,15 0,15" fill="var(--maroon)"/><polygon points="140,0 147,0 162,15 155,15" fill="#bdbdbd"/></svg><span>www.website.com</span></div>
  <div class="pageno">1</div>
</section>

<!-- Our services -->
<section class="slide c3 r1">
  <div class="title">OUR SERVICES</div>
  <div class="rule"></div>
  <div class="subtitle" style="top:40px">Lorem ipsum dolor sit amet, consectetuer adipiscing elit, sed diam</div>
  <div class="svc-icon" style="left:33px;top:84px"><div><svg width="24" height="20" viewBox="0 0 24 20"><path d="M2 6l5-3 5 3 5-3 5 3v4l-7 6-3-3-3 3-7-6z" fill="none" stroke="#fff" stroke-width="1.6" stroke-linejoin="round"/></svg></div></div>
  <div class="svc-icon" style="left:112px;top:84px"><div><svg width="22" height="22" viewBox="0 0 22 22"><path d="M4 12a7 7 0 0 1 14 0" fill="none" stroke="#fff" stroke-width="1.8"/><rect x="2" y="11" width="4" height="6" rx="1" fill="#fff"/><rect x="16" y="11" width="4" height="6" rx="1" fill="#fff"/><circle cx="11" cy="12" r="3.5" fill="#fff"/></svg></div></div>
  <div class="svc-icon" style="left:196px;top:84px"><div><svg width="20" height="22" viewBox="0 0 20 22"><rect x="3" y="2" width="14" height="18" rx="1" fill="none" stroke="#fff" stroke-width="1.6"/><path d="M6 8h8M6 12h8M6 16h5" stroke="#fff" stroke-width="1.4"/></svg></div></div>
  <div class="svc-icon" style="left:279px;top:84px"><div><svg width="22" height="20" viewBox="0 0 22 20"><rect x="3" y="11" width="4" height="7" fill="#fff"/><rect x="9" y="8" width="4" height="10" fill="#fff"/><rect x="15" y="5" width="4" height="13" fill="#fff"/><path d="M2 8l7-4 4 2 7-4" fill="none" stroke="#fff" stroke-width="1.4"/></svg></div></div>
  <div class="svc-text" style="left:19px;top:140px">Lorem Ipsum is simply dummy text of the print-ing and typesetting industry. Lorem Ipsum has been Lorem Ipsum is simply dummy text of the printing and typesetting industry. Lorem Ipsum</div>
  <div class="svc-text" style="left:98px;top:140px">Lorem Ipsum is simply dummy text of the print-ing and typesetting industry. Lorem Ipsum has been Lorem Ipsum is simply dummy text of the printing and typesetting industry. Lorem Ipsum</div>
  <div class="svc-text" style="left:182px;top:140px">Lorem Ipsum is simply dummy text of the print-ing and typesetting industry. Lorem Ipsum has been Lorem Ipsum is simply dummy text of the printing and typesetting industry. Lorem Ipsum</div>
  <div class="svc-text" style="left:265px;top:140px">Lorem Ipsum is simply dummy text of the print-ing and typesetting industry. Lorem Ipsum has been Lorem Ipsum is simply dummy text of the printing and typesetting industry. Lorem Ipsum</div>
  <div class="footer"><svg width="180" height="15"><polygon points="0,0 140,0 155,15 0,15" fill="var(--maroon)"/><polygon points="140,0 147,0 162,15 155,15" fill="#bdbdbd"/></svg><span>www.website.com</span></div>
  <div class="pageno">3</div>
</section>

<!-- What we do -->
<section class="slide c1 r2">
  <div class="title">WHAT WE DO</div>
  <div class="rule"></div>
  <div class="wwd-photo" role="img" aria-label="Businessman in a suit" style="left:43px;top:50px;background:radial-gradient(circle at 50% 60%,#2d2d33 0 40%,#e9ecef 41%)"></div>
  <div class="wwd-photo" role="img" aria-label="Businesswoman at a desk" style="left:144px;top:50px;background:radial-gradient(circle at 50% 60%,#3a302a 0 40%,#e8e8e8 41%)"></div>
  <div class="wwd-photo" role="img" aria-label="Stack of files and folders" style="left:261px;top:50px;background:radial-gradient(circle at 50% 55%,#7ea4c8 0 38%,#eef1f4 39%)"></div>
  <div class="wwd-box" style="left:20px;width:102px"><h4>Lorem ipsum dolor sit amet, consectetur adipisic-</h4><p>Lorem Ipsum is simply dummy text of the printing and typeset-ting industry. Lorem Ipsum has been the industry's standard dummy text ever since the 1500s, when an unknown printer took a galley of type and scrambled it to make a type specimen book. It has survived not only five centu-ries, but also the leap into elec-tronic typesetting, remaining essentially unchanged. It was popularised in the 1960s with the</p></div>
  <div class="wwd-box" style="left:132px;width:102px"><h4>Lorem ipsum dolor sit amet, consectetur adipisic-</h4><p>Lorem Ipsum is simply dummy text of the printing and typeset-ting industry. Lorem Ipsum has been the industry's standard dummy text ever since the 1500s, when an unknown printer took a galley of type and scrambled it to make a type specimen book. It has survived not only five centu-ries, but also the leap into elec-tronic typesetting, remaining essentially unchanged. It was</p></div>
  <div class="wwd-box" style="left:246px;width:94px"><h4>Lorem ipsum dolor sit amet, consectetur adipisic-</h4><p>Lorem Ipsum is simply dummy text of the printing and typeset-ting industry. Lorem Ipsum has been the industry's standard dummy text ever since the 1500s, when an unknown printer took a galley of type and scrambled it to make a type specimen book. It has survived not only five centu-ries, but also the leap into elec-tronic typesetting, remaining essentially unchanged. It was</p></div>
  <div class="footer"><svg width="180" height="15"><polygon points="0,0 120,0 135,15 0,15" fill="var(--maroon)"/><polygon points="120,0 127,0 142,15 135,15" fill="#bdbdbd"/></svg><span>www.website.com</span></div>
</section>

<!-- Picture slide -->
<section class="slide c2 r2">
  <div class="title">PICTURE SLIDE</div>
  <div class="rule"></div>
  <div class="photo" role="img" aria-label="Hand sketching a cloud network diagram" style="left:20px;top:42px;width:164px;height:105px;background:linear-gradient(120deg,#9fb3c6,#2e4a6b 55%,#c8d3dc)"></div>
  <div class="photo" role="img" aria-label="Relaxed businessman at a laptop" style="left:20px;top:149px;width:72px;height:79px;background:linear-gradient(#eef0f2,#c7cbd0 60%,#3a3c42)"></div>
  <div class="photo" role="img" aria-label="Man working at a computer screen" style="left:94px;top:149px;width:90px;height:79px;background:linear-gradient(120deg,#dfe5ea,#b8c3cc 50%,#4c5a6a)"></div>
  <div class="ps-icon" style="left:203px;top:43px"><span></span></div>
  <div class="ps-head" style="left:227px;top:44px">Lorem ipsum dolor sit amet,</div>
  <div class="ps-body" style="left:227px;top:58px">Lorem Ipsum is simply dummy text of the printing and typesetting industry. Lorem Ipsum has been the industry's standard dummy text ever since the 1500s, when an unknown printer took a galley of type and scrambled it to make a type specimen book. It has survived not only five centuries, but also the leap into electronic typesetting, remaining essentially unchanged. It was popularised in</div>
  <div class="ps-icon" style="left:203px;top:145px"><span></span></div>
  <div class="ps-head" style="left:227px;top:146px">Lorem ipsum dolor sit amet,</div>
  <div class="ps-body" style="left:227px;top:164px">Lorem Ipsum is simply dummy text of the printing and typesetting industry. Lorem Ipsum has been the industry's standard dummy text ever since the 1500s, when an unknown printer took a galley of type and scrambled it to make a type specimen book. It has survived not only five centuries, but also</div>
  <div class="footer"><svg width="180" height="15"><polygon points="0,0 120,0 135,15 0,15" fill="var(--maroon)"/><polygon points="120,0 127,0 142,15 135,15" fill="#bdbdbd"/></svg><span>www.website.com</span></div>
</section>

<!-- Bullet text -->
<section class="slide c3 r2">
  <div class="title">BULLET TEXT</div>
  <div class="rule"></div>
  <div class="abs" style="left:21px;top:38px;width:320px;font-size:4.6px;line-height:8px;color:#222">Lorem Ipsum is simply dummy text of the printing and typesetting industry. Lorem Ipsum has been the industry's standard dummy text ever since the 1500s, when an unknown printer took a galley of type and scrambled it to make a type specimen book. It has survived not only five centuries, but also the leap into electronic typesetting, remaining essentially unchanged. It was popularised in the 1960s</div>
  <div class="photo" role="img" aria-label="Relaxed businessman leaning back at his laptop" style="left:30px;top:111px;width:188px;height:129px;background:linear-gradient(90deg,#dfe6ee,#f3f5f7 45%,#c9d2dc)"></div>
  <div class="bullet" style="top:76px">Lorem Ipsum is simply dummy text of the printing and typesetting industry. Lorem Ipsum has been the industry's standard dummy tex</div>
  <div class="bullet" style="top:104px">Ever since the 1500s, when an unknown printer took a galley of type and scrambled it to make a type specimen book.</div>
  <div class="bullet" style="top:131px">It has survived not only five centuries, but also the leap into electronic typesetting, remaining essentially unchanged. It was popularised in the 1960s with the release of</div>
  <div class="bullet" style="top:166px">It is a long established fact that a reader will be distracted by the readable content of a page when looking at its layout. The point of using</div>
  <div class="bullet" style="top:193px">Lorem Ipsum is that it has a more-or-less normal distribution of letters, as opposed to using 'Content here, content here', making it look like readable English. Many desktop publishing packages and web page editors now use Lorem Ipsum as their default model text, and a search for 'lorem ipsum' will uncover many web sites still in their infancy. Vari</div>
  <div class="footer"><svg width="180" height="15"><polygon points="0,0 120,0 135,15 0,15" fill="var(--maroon)"/><polygon points="120,0 127,0 142,15 135,15" fill="#bdbdbd"/></svg><span>www.website.com</span></div>
</section>

<!-- Chart slide -->
<section class="slide c1 r3">
  <div class="title">YOUR HEADLINE HERE TO PUT</div>
  <div class="rule"></div>
  <div class="subtitle" style="top:46px">Lorem ipsum dolor sit amet, consectetur adipisicing do eiusmod</div>
  <div class="chart-title" style="top:79px">USE OF FOUNDER SEED CAPITAL<br>$1.12M SINCE JAN 2014</div>
  <div class="legend"><span class="lg-m">marketing</span><span class="lg-s">sg&amp;a</span><span class="lg-r">r&amp;d</span><span class="lg-l">1x legal</span></div>
  <svg class="abs" style="left:50px;top:124px" width="110" height="110" viewBox="0 0 110 110">
    <g transform="rotate(-90 55 55)" fill="none" stroke-width="30">
      <circle cx="55" cy="55" r="40" stroke="var(--blue)" stroke-dasharray="30.16 251.33"/>
      <circle cx="55" cy="55" r="40" stroke="var(--orange)" stroke-dasharray="52.78 251.33" stroke-dashoffset="-30.16"/>
      <circle cx="55" cy="55" r="40" stroke="var(--grey)" stroke-dasharray="150.8 251.33" stroke-dashoffset="-82.94"/>
      <circle cx="55" cy="55" r="40" stroke="var(--gold)" stroke-dasharray="17.59 251.33" stroke-dashoffset="-233.74"/>
    </g>
    <g font-size="6" fill="#fff" font-family="Open Sans, sans-serif" text-anchor="middle">
      <text x="70" y="19">marketing</text><text x="70" y="26">12%</text>
      <text x="91" y="50">sg&amp;a</text><text x="91" y="57">21%</text>
      <text x="26" y="86">r&amp;d</text><text x="26" y="93">60%</text>
      <text x="47" y="16">1x legal</text><text x="47" y="23">7%</text>
    </g>
  </svg>
  <div class="body-just" style="top:72px">Lorem Ipsum is simply dummy text of the printing and typesetting industry. Lorem Ipsum has been the industry's standard dummy text ever since the 1500s, when an unknown printer took a galley of type and scrambled it to make a type specimen book. It has survived not only five centuries, but also the leap into electronic typesetting, remaining essentially unchanged. It was popularised in the 1960s with the release of Letraset sheets containing Lorem Ipsum passages, and more recently with desktop publishing software like Aldus PageMaker including versions of Lorem Ipsum.</div>
  <div class="body-just" style="top:175px">It is a long established fact that a reader will be distracted by the readable content of a page when looking at its layout. The point of using Lorem Ipsum is that it has a more-or-less normal distribution of letters, as opposed to using 'Content here, content here', making it look like readable English. Many desktop publishing packages and web page editors now use Lorem Ipsum as their default model text,</div>
  <div class="footer"><svg width="180" height="15"><polygon points="0,0 120,0 135,15 0,15" fill="var(--maroon)"/><polygon points="120,0 127,0 142,15 135,15" fill="#bdbdbd"/></svg><span>www.website.com</span></div>
  <div class="pageno">2</div>
</section>

<!-- Closing -->
<section class="slide c2 r3">
  <div class="gband" style="top:38px;height:6px"></div>
  <div class="photo" role="img" aria-label="Dimmed dirt road under construction" style="left:0;top:48px;width:127px;height:50px;background:linear-gradient(#4a5560 0 35%,#5c4634 35%,#4a3628)"></div>
  <div class="photo" role="img" aria-label="Dimmed curving road through bush" style="left:129px;top:48px;width:81px;height:50px;background:linear-gradient(160deg,#3a4530,#4f5550 60%,#3e403e)"></div>
  <div class="photo" role="img" aria-label="Dimmed residential houses" style="left:212px;top:48px;width:61px;height:50px;background:linear-gradient(#56606a,#5a5a58 55%,#3a3b38)"></div>
  <div class="photo" role="img" aria-label="Dimmed brick apartment block" style="left:275px;top:48px;width:81px;height:50px;background:linear-gradient(#4c5a6c,#4a3328 50%,#241c18)"></div>
  <div class="photo" role="img" aria-label="Dimmed office building under construction" style="left:0;top:100px;width:223px;height:85px;background:linear-gradient(#4a5a70,#5a6068 45%,#454542 65%,#4e3e2e)"></div>
  <div class="photo" role="img" aria-label="Dimmed company signboard at housing estate" style="left:226px;top:100px;width:130px;height:85px;background:linear-gradient(#565e64,#4e5246 45%,#5c4c42 75%,#383e28)"></div>
  <div class="gband" style="top:187px;height:5px"></div>
  <div class="brand" style="left:22px;top:219px;width:70px"><b style="font-size:12px">VELDMARK</b><i style="font-size:8px">Properties</i></div>
  <div class="contact" style="left:94px;top:220px">P: +00 915 000 0100<br>F: +00 121 000 0200</div>
  <div class="vline" style="left:163px;top:222px;height:22px"></div>
  <div class="contact" style="left:173px;top:220px">info@veldmark.com<br>www.veldmark.com</div>
  <div class="vline" style="left:260px;top:222px;height:22px"></div>
  <div class="contact" style="left:270px;top:220px">P.O. Box 0000, Elm<br>Town 0000, xxx</div>
</section>

</body>
</html>
```